Brookfarrow Osteopathy and dry needling business card

Business card for Brookfarrow Osteopathy and Dry Needling.

Industry/Entity Type

Health

Contact Information for Business Card

I do not have a phone number yet. I also do not have an email address yet. The physical address is: 48 Lower Crane Street Brookfarrow The website is: www.brookfarrowosteosteopathy.example My details are: Dr Martin Pellowe, Osteopath (B.Clin.Sci (Ost) M.Ost BSC ECON (Hons)

Colors
0094D4
00A9DD
6FCCEA
C7EBF8
E9F6FB

Requirements
Must have
• logo on the back
Nice to have
• Maybe a space for me to write an appointment time and date on the card.

```html
<!DOCTYPE html>
<html lang="en">
<head>
<meta charset="utf-8">
<title>Brookfarrow Osteopathy and Dry Needling – Business Card</title>
<link rel="stylesheet" href="https://fonts.googleapis.com/css2?family=Montserrat:wght@400;500;600&family=Arimo:wght@400;700&display=swap">
<style>
  :root {
    --stage: #1c1c1e;
    --card-dark: #2b2b2d;
    --card-dark-edge: #333336;
    --paper: #ffffff;
    --brand-blue: #0094d4;
    --brand-cyan: #00a9dd;
    --line-grey: #b9b9bb;
    --label-grey: #5a5a5c;
    --text-light: #f2f2f2;
  }
  * { margin: 0; padding: 0; box-sizing: border-box; }
  html, body { width: 1200px; height: 886px; overflow: hidden; }
  body {
    background: var(--stage);
    font-family: "Montserrat", sans-serif;
    position: relative;
  }
  .card {
    position: absolute;
    width: 540px;
    height: 316px;
    border-radius: 22px;
    overflow: hidden;
    box-shadow: 0 18px 40px rgba(0,0,0,0.55);
  }

  /* ---------- Appointment side ---------- */
  .card--appointment { left: 50px; top: 110px; background: var(--paper); }
  .appointment__head {
    position: absolute; inset: 0 0 auto 0; height: 122px;
    background: var(--card-dark);
  }
  .appointment__brand {
    position: absolute; top: 20px; left: 0; right: 0;
    display: flex; flex-direction: column; align-items: center; gap: 6px;
    color: var(--brand-cyan); font-size: 12px; font-weight: 600; letter-spacing: 0.3px;
  }
  .brand-dot {
    width: 36px; height: 36px; border-radius: 50%;
    border: 2px solid var(--brand-cyan);
  }
  .appointment__band { position: absolute; left: 0; top: 100px; width: 540px; height: 60px; }
  .appointment__title {
    position: absolute; top: 122px; left: 0; right: 0; text-align: center;
    color: var(--paper); font-size: 15px; font-weight: 500; letter-spacing: 0.8px;
    line-height: 18px;
  }
  .appointment__form { position: absolute; left: 40px; right: 40px; top: 186px; }
  .form-rule { height: 1px; background: var(--line-grey); }
  .day-row {
    display: flex; justify-content: space-between; margin: 22px 0 20px;
  }
  .check {
    display: flex; align-items: center; gap: 8px;
    font-size: 13px; color: var(--label-grey); letter-spacing: 0.6px;
  }
  .check::before {
    content: ""; width: 12px; height: 12px;
    border: 2px solid var(--brand-cyan);
  }
  .field-row { display: flex; align-items: flex-end; gap: 10px; }
  .field-label { font-size: 13px; color: var(--label-grey); letter-spacing: 0.6px; }
  .field-line { flex: 1; height: 1px; background: var(--line-grey); margin-bottom: 4px; }
  .field-row .check { margin-left: 6px; }

  /* ---------- Contact side ---------- */
  .card--contact {
    left: 610px; top: 450px;
    background: linear-gradient(160deg, var(--card-dark-edge), var(--card-dark));
    font-family: "Arimo", sans-serif;
  }
  .contact__brand {
    position: absolute; top: 26px; right: 30px; width: 200px;
    display: flex; flex-direction: column; align-items: center; gap: 10px;
    text-align: center;
    color: var(--brand-cyan); font-size: 15px; font-weight: 700; line-height: 1.3;
  }
  .contact__brand .brand-dot { width: 70px; height: 70px; border-width: 3px; }
  .contact__person { position: absolute; left: 30px; top: 122px; }
  .person__name { color: var(--brand-cyan); font-size: 21px; font-weight: 700; line-height: 24px; }
  .person__quals { color: var(--text-light); font-size: 13.5px; line-height: 1.35; margin-top: 6px; }
  .contact__rule { position: absolute; left: 28px; right: 28px; top: 204px; height: 1px; background: var(--brand-blue); }
  .contact__list { position: absolute; left: 30px; top: 218px; list-style: none; }
  .contact__list li {
    display: flex; align-items: center; gap: 8px;
    color: var(--text-light); font-size: 13.5px; line-height: 26px;
  }
  .contact__list svg { width: 14px; height: 14px; fill: var(--brand-cyan); }
  .contact__address {
    position: absolute; right: 30px; top: 222px; text-align right;
    text-align: right; font-style: normal;
    color: var(--text-light); font-size: 14px; line-height: 1.4;
  }
</style>
</head>
<body>

<section class="card card--appointment" aria-label="Appointment side">
  <div class="appointment__head"></div>
  <div class="appointment__brand"><span class="brand-dot"></span>Brookfarrow Osteopathy and Dry Needling</div>
  <svg class="appointment__band" viewBox="0 0 540 60" aria-hidden="true">
    <polygon points="0,18 150,18 172,42 368,42 390,18 540,18 540,24 394,24 372,48 168,48 146,24 0,24" fill="#0094d4"/>
    <polygon points="150,18 390,18 368,42 172,42" fill="#00a9dd"/>
  </svg>
  <div class="appointment__title">APPOINTMENT</div>

  <div class="appointment__form">
    <div class="form-rule"></div>
    <div class="day-row">
      <span class="check">MON</span>
      <span class="check">TUE</span>
      <span class="check">WED</span>
      <span class="check">THU</span>
      <span class="check">FRI</span>
      <span class="check">SAT</span>
    </div>
    <div class="field-row">
      <span class="field-label">DATE</span><span class="field-line"></span>
      <span class="field-label">TIME</span><span class="field-line"></span>
      <span class="check">AM</span>
      <span class="check">PM</span>
    </div>
  </div>
</section>

<section class="card card--contact" aria-label="Contact side">
  <div class="contact__brand"><span class="brand-dot"></span>Brookfarrow Osteopathy and Dry Needling</div>

  <div class="contact__person">
    <div class="person__name">Dr Martin Pellowe</div>
    <div class="person__quals">Osteopath (B.Clin.Sci (Ost)<br>M.Ost BSC ECON (Hons)</div>
  </div>
  <div class="contact__rule"></div>

  <ul class="contact__list">
    <li><svg viewBox="0 0 16 16" aria-hidden="true"><path d="M3 1l3 3-2 2c1 2 3 4 5 5l2-2 3 3-2 2C7 14 2 9 1 3z"/></svg>555-014-7730</li>
    <li><svg viewBox="0 0 16 16" aria-hidden="true"><path d="M1 3h14v10H1zM2 4l6 5 6-5v-.5H2z"/></svg>hello@brookfarrow.example</li>
    <li><svg viewBox="0 0 16 16" aria-hidden="true"><circle cx="8" cy="8" r="7"/></svg>www.brookfarrowosteosteopathy.example</li>
  </ul>

  <address class="contact__address">48 Lower Crane Street<br>Brookfarrow</address>
</section>

</body>
</html>
```